Business Card and Letterhead for Nurlo - modern real estate business

I need a double sided business card design for Nurlo. Please see business card brief here https://papers.trelvimo.net/sheet/q/7XrTbaLeZpMmQ2uWvd9HkCj4yNoEfsGi3lRtAz_pk/view?mode=shared

Please feel free to design the business cards however you feel best. I am happy to give some creative freedoms and then provide feedback from there.

Please then also create a letterhead to match the business card design

Colors

Designer to choose colors to be used in the design.

Requirements
Must have
• Must be a modern, elegant business card which looks very professional

```html
<!DOCTYPE html>
<html lang="en">
<head>
<meta charset="utf-8">
<title>Nurlo – Business Card</title>
<link rel="stylesheet" href="https://fonts.googleapis.com/css2?family=Oswald:wght@400;500&family=Yellowtail&display=swap">
<style>
  :root {
    --ink: #000000;
    --paper: #ffffff;
    --brand-red: #e3141f;
    --band-red-dark: #3a0a0d;
    --band-red: #6b1117;
    --globe-deep: #06203a;
    --globe-mid: #1a5f8c;
    --globe-light: #5fb2dc;
    --photo-dark: #0d0d0d;
    --photo-mid: #2b2b2d;
  }
  html, body {
    margin: 0;
    padding: 0;
    width: 1200px;
    height: 686px;
    overflow: hidden;
    background: var(--ink);
  }
  .card {
    position: relative;
    width: 1200px;
    height: 686px;
    background: var(--ink);
    overflow: hidden;
  }
  .card-art {
    position: absolute;
    inset: 0;
  }
  .brand-name {
    position: absolute;
    left: 776px;
    top: 128px;
    width: 326px;
    margin: 0;
    text-align: center;
    font-family: "Oswald", sans-serif;
    font-weight: 500;
    font-size: 68px;
    line-height: 1;
    letter-spacing: 10px;
    color: var(--brand-red);
  }
  .agent-name {
    position: absolute;
    left: 788px;
    top: 226px;
    width: 300px;
    margin: 0;
    text-align: center;
    font-family: "Yellowtail", cursive;
    font-weight: 400;
    font-size: 50px;
    line-height: 1;
    color: var(--paper);
  }
  .agent-role {
    position: absolute;
    left: 788px;
    top: 290px;
    width: 300px;
    margin: 0;
    text-align: center;
    font-family: "Yellowtail", cursive;
    font-size: 23px;
    line-height: 1;
    color: var(--paper);
  }
  .contact-list {
    list-style: none;
    margin: 0;
    padding: 0;
  }
  .contact-item {
    position: absolute;
    left: 797px;
    display: flex;
    align-items: center;
    gap: 40px;
  }
  .contact-icon {
    width: 54px;
    height: 54px;
    flex: none;
  }
  .contact-text {
    font-family: "Oswald", sans-serif;
    font-weight: 400;
    font-size: 29px;
    line-height: 1.3;
    letter-spacing: 1px;
    color: var(--paper);
  }
  .contact-phone { top: 342px; }
  .contact-email { top: 428px; }
  .contact-address { top: 511px; }
  .contact-web { top: 595px; }
</style>
</head>
<body>
<main class="card">
  <svg class="card-art" width="1200" height="686" viewBox="0 0 1200 686" aria-hidden="false">
    <defs>
      <radialGradient id="globe-tones" cx="0.25" cy="0.45" r="0.8">
        <stop offset="0" stop-color="var(--globe-light)"/>
        <stop offset="0.5" stop-color="var(--globe-mid)"/>
        <stop offset="1" stop-color="var(--globe-deep)"/>
      </radialGradient>
      <linearGradient id="band-tones" x1="0" y1="0" x2="1" y2="1">
        <stop offset="0" stop-color="var(--band-red)"/>
        <stop offset="1" stop-color="var(--band-red-dark)"/>
      </linearGradient>
      <linearGradient id="photo-tones" x1="0" y1="0" x2="0" y2="1">
        <stop offset="0" stop-color="var(--photo-mid)"/>
        <stop offset="1" stop-color="var(--photo-dark)"/>
      </linearGradient>
    </defs>

    <path class="accent-band" fill="url(#band-tones)"
      d="M215,0 H330 L205,185 Q170,240 205,290 L535,686 H455 L118,280 C120,230 175,140 215,0 Z"/>

    <path class="globe-panel" role="img" aria-label="Glowing blue globe with network connection lines"
      fill="url(#globe-tones)"
      d="M0,0 H215 C175,140 120,230 118,280 L455,686 H0 Z"/>

    <path class="accent-line" fill="none" stroke="var(--brand-red)" stroke-width="3"
      d="M222,0 C182,140 127,230 125,280 L462,686"/>

    <path class="agent-photo" role="img" aria-label="Portrait photo of the agent in a dark suit"
      fill="url(#photo-tones)"
      d="M330,686 V420 C330,330 380,290 430,280 C430,160 470,80 520,80 C575,80 610,160 605,280 C660,290 735,330 760,420 L775,686 Z"/>
  </svg>

  <h1 class="brand-name">NURLO</h1>
  <p class="agent-name">Liam Hartley</p>
  <p class="agent-role">Licenced Real Estate Agent</p>

  <ul class="contact-list">
    <li class="contact-item contact-phone">
      <svg class="contact-icon" viewBox="0 0 54 54" aria-hidden="true">
        <circle cx="27" cy="27" r="27" fill="var(--paper)"/>
        <path fill="var(--ink)" d="M19,15 l5,-1 l4,8 l-3,3 c1,3 4,6 7,7 l3,-3 l8,4 l-1,5 c-1,2 -3,3 -5,3 c-11,-1 -20,-10 -21,-21 c0,-2 1,-4 3,-5 z"/>
      </svg>
      <span class="contact-text">0412 583 904</span>
    </li>
    <li class="contact-item contact-email">
      <svg class="contact-icon" viewBox="0 0 54 54" aria-hidden="true">
        <circle cx="27" cy="27" r="27" fill="var(--paper)"/>
        <rect x="15" y="18" width="24" height="18" fill="var(--ink)"/>
        <path fill="none" stroke="var(--paper)" stroke-width="2" d="M15,18 L27,28 L39,18 M15,36 L24,26 M39,36 L30,26"/>
      </svg>
      <span class="contact-text">LIAM@NURLO.COM</span>
    </li>
    <li class="contact-item contact-address">
      <svg class="contact-icon" viewBox="0 0 54 54" aria-hidden="true">
        <circle cx="27" cy="27" r="27" fill="var(--paper)"/>
        <path fill="none" stroke="var(--ink)" stroke-width="2.5" d="M27,40 C20,31 18,27 18,23 a9,9 0 0 1 18,0 c0,4 -2,8 -9,17 z"/>
        <circle cx="27" cy="23" r="3.5" fill="none" stroke="var(--ink)" stroke-width="2.5"/>
      </svg>
      <span class="contact-text">PO Box 3170<br>Glenmora NSW 2790</span>
    </li>
    <li class="contact-item contact-web">
      <svg class="contact-icon" viewBox="0 0 54 54" aria-hidden="true">
        <circle cx="27" cy="27" r="27" fill="var(--paper)"/>
        <g fill="none" stroke="var(--ink)" stroke-width="2">
          <circle cx="27" cy="27" r="12"/>
          <ellipse cx="27" cy="27" rx="5" ry="12"/>
          <path d="M15,27 H39 M17,21 H37 M17,33 H37"/>
        </g>
      </svg>
      <span class="contact-text">WWW.NURLO.COM</span>
    </li>
  </ul>
</main>
</body>
</html>
```